NZ First of it's kind solutions directory and marketplace for busy Mums needs a business card design

We need a business card design for our new nationwide business in NZ (long term plans to go global). We provide solutions to the everyday challenges that busy Mums face by connecting them with quality communities and suppliers of carefully selected, relevant products and services. We sell direct via our online marketplace. The final design should communicate our values of inclusivity, quality and smart solutions. Colours should incorporate our logo colour palette of #477077 and #6ba8b2. Our website is at https://www.brightnestly.com

Target Market(s)

busy Mums, Age 28 – 50, female, income over $100K, location main centres NZ primarily but NZ wide. Is likely juggling work or career with a young family. Probably had hobbies which have fallen by the wayside.
-Wants to succeed in her chosen career without compromising on family life
-to successfully juggle her career without feeling like she is compromising her children
- Is time poor, something always has to give and it’s generally her health (she’ll stay up late, get stressed)
- probably ex corporate or professional career. Has discretional income

Industry/Entity Type

Business

Contact Information for Business Card

Jodie Farnsworth, Founder, BrightNestly.com (Strapline Browse; Pick; Sorted), 48 Kowhai Terrace, Hillsborough, Auckland 1058, New Zealand. Mob: 021 437 518 Ph: +64 (0)9 584 7163

Font styles to use
Other font styles liked:
• Raleway, and/or Architects Daughter

Colors
00a990
33b8a4
86cfc6
cfeae6

Requirements
Must have
• the above details, streamline. the logo and colours associated with those logos
Should not have
• foil or metallic colours

```html
<!DOCTYPE html>
<html lang="en">
<head>
<meta charset="utf-8">
<title>BrightNestly — Business Card</title>
<link rel="stylesheet" href="https://fonts.googleapis.com/css2?family=Architects+Daughter&family=Raleway:wght@400;500;800&display=swap">
<style>
  :root {
    --brand-deep: #477077;
    --brand-soft: #6ba8b2;
    --band: #4f97a0;
    --card: #eeeff1;
    --backdrop: #d9dcdf;
    --ink: #4a4d50;
    --white: #ffffff;
  }
  * { box-sizing: border-box; margin: 0; padding: 0; }
  html, body { width: 1200px; height: 800px; overflow: hidden; }
  body {
    background: var(--backdrop);
    font-family: "Raleway", sans-serif;
    display: flex;
    align-items: center;
    justify-content: center;
    gap: 40px;
  }
  .card {
    position: relative;
    width: 540px;
    height: 310px;
    background: var(--card);
    box-shadow: 0 6px 18px rgba(0,0,0,0.18);
    overflow: hidden;
  }

  /* Front */
  .card-front .wordmark {
    position: absolute;
    top: 110px;
    left: 0;
    right: 0;
    display: flex;
    align-items: center;
    justify-content: center;
    gap: 16px;
  }
  .wordmark-dot {
    width: 40px;
    height: 40px;
    border-radius: 50%;
    background: var(--brand-deep);
  }
  .wordmark-name {
    font-weight: 800;
    font-size: 50px;
    letter-spacing: -0.5px;
    color: var(--brand-deep);
  }
  .card-front .address {
    position: absolute;
    left: 34px;
    bottom: 30px;
    font-size: 14px;
    color: var(--ink);
  }

  /* Back */
  .card-back .details {
    position: absolute;
    top: 0; left: 0; bottom: 0;
    width: 395px;
  }
  .person {
    position: absolute;
    top: 36px;
    left: 0; right: 0;
    text-align: center;
  }
  .person-name {
    font-weight: 800;
    font-size: 29px;
    color: var(--brand-deep);
    letter-spacing: 0.5px;
    text-transform: uppercase;
  }
  .person-role {
    font-weight: 500;
    font-size: 14px;
    color: var(--ink);
    letter-spacing: 1px;
    text-transform: uppercase;
    margin-top: 2px;
  }
  .mark {
    position: absolute;
    top: 128px;
    left: 50%;
    transform: translateX(-50%);
    width: 36px;
    height: 36px;
    border-radius: 50%;
    background: var(--brand-deep);
  }
  .contact {
    position: absolute;
    left: 26px;
    right: 10px;
    bottom: 32px;
    font-size: 14.5px;
    color: var(--ink);
    line-height: 1.45;
  }
  .contact .web { text-align: center; }
  .band {
    position: absolute;
    top: 0; right: 0; bottom: 0;
    width: 145px;
    background: var(--band);
  }
  .strapline {
    position: absolute;
    left: 42px;
    bottom: 22px;
    transform-origin: left bottom;
    transform: rotate(-90deg) translateY(100%);
    white-space: nowrap;
    font-family: "Architects Daughter", cursive;
    font-size: 21px;
    color: var(--white);
    letter-spacing: 0.5px;
  }
</style>
</head>
<body>
  <section class="card card-front">
    <div class="wordmark">
      <span class="wordmark-dot"></span>
      <span class="wordmark-name">BrightNestly</span>
    </div>
    <p class="address">48 Kowhai Terrace, Hillsborough, Auckland 1058, New Zealand</p>
  </section>

  <section class="card card-back">
    <div class="details">
      <div class="person">
        <h1 class="person-name">Jodie Farnsworth</h1>
        <p class="person-role">Founder</p>
      </div>
      <span class="mark"></span>
      <div class="contact">
        <p>Mob: 021 437 518 &nbsp;|&nbsp; Ph: +64 (0)9 584 7163</p>
        <p class="web">www.brightnestly.com</p>
      </div>
    </div>
    <div class="band">
      <p class="strapline">Browse - Pick - Sorted</p>
    </div>
  </section>
</body>
</html>
```